Business Card Design

We need a new business card design for a CPA office that has been in business for over 10 years. We are a Accounting Concierge firm that offers the following services: Certified Public Accountant, Personal & Business Tax Preparation, Accounting, Bookkeeping, Payroll Services, Tax Litigation Services.
Certified LedgerNest TallyPartner.  We would like to see designs that use the color navy blue in the company logo with classic accent colors.  We would like the card to be on a textured high pound card stock and that is more classic and less modern in design.  The final design should communicate class and professionalism.

Updates
Reason: I gave feedback to many of the designers with some changes.  Please re-read the brief as we would like to remove the photo of the man on the card.  We also want only light grey or white background, not navy or blue - the navy or blue tones should be the font or accent colors.  Please also, consider creating a logo with the initials P&A or PA or P&A CPA.

Industry/Entity Type
Business
Contact Information for Business Card
Pelwick & Associates CPA, Gerald Pelwick III, 5136 Orvale Road West, Suite D, Larkmoor, GA  34917, Phone: (555) 318-2276, Fax: (555) 462-7093, Email: Gerald@GPelwickCPA.example, Website: www.GPelwickCPA.example
Requirements
Must have
- LedgerNest Logo

Should not have
- we no longer want the photo on the card.

```html
<!DOCTYPE html>
<html lang="en">
<head>
<meta charset="utf-8">
<title>Pelwick &amp; Associates CPA – Business Card</title>
<link rel="stylesheet" href="https://fonts.googleapis.com/css2?family=Montserrat:ital,wght@0,400;0,500;0,700;1,400;1,700&display=swap">
<style>
  :root {
    --backdrop: #d6d6d8;
    --card: #f3f3f4;
    --card-edge: #c4c4c8;
    --navy: #2b2a7c;
  }
  * { margin: 0; padding: 0; box-sizing: border-box; }
  html, body {
    width: 1200px;
    height: 720px;
    overflow: hidden;
    background: var(--backdrop);
    font-family: "Montserrat", sans-serif;
    color: var(--navy);
  }
  .business-card {
    position: absolute;
    left: 100px;
    top: 74px;
    width: 1000px;
    height: 572px;
    background: var(--card);
    border: 1px solid var(--card-edge);
    box-shadow: 0 10px 28px rgba(0, 0, 0, 0.18);
  }
  .brand {
    position: absolute;
    top: 78px;
    left: 0;
    right: 0;
    display: flex;
    justify-content: center;
    align-items: center;
    gap: 22px;
  }
  .brand-square {
    width: 72px;
    height: 72px;
    background: var(--navy);
    flex: none;
  }
  .brand-text { display: flex; flex-direction: column; align-items: center; }
  .brand-name {
    font-weight: 700;
    font-size: 33px;
    letter-spacing: 1.5px;
    text-transform: uppercase;
    line-height: 1.1;
  }
  .brand-tagline {
    font-weight: 400;
    font-size: 25px;
    letter-spacing: 1.5px;
    line-height: 1.25;
  }
  .holder {
    position: absolute;
    left: 88px;
    top: 302px;
    font-size: 27px;
    font-style: italic;
    font-weight: 400;
    letter-spacing: 0.5px;
  }
  .holder strong { font-weight: 700; }
  .contact-list {
    position: absolute;
    left: 70px;
    top: 372px;
    list-style: none;
    font-size: 23px;
    font-style: italic;
    line-height: 1.5;
    letter-spacing: 0.3px;
  }
  .contact-list li:nth-child(1) { padding-left: 18px; }
  .contact-list li:nth-child(2) { padding-left: 8px; }
  .contact-list li:nth-child(3) { margin-top: 6px; }
  .contact-list strong { font-weight: 700; }
  .address {
    position: absolute;
    right: 70px;
    top: 362px;
    text-align: right;
    font-style: normal;
    font-weight: 700;
    font-size: 22px;
    line-height: 1.4;
    letter-spacing: 0.3px;
  }
</style>
</head>
<body>
  <section class="business-card" aria-label="Business card">
    <header class="brand">
      <div class="brand-square" aria-hidden="true"></div>
      <div class="brand-text">
        <h1 class="brand-name">Pelwick &amp; Associates CPA</h1>
        <p class="brand-tagline">Certified Public Accountant</p>
      </div>
    </header>

    <p class="holder">Gerald<strong>Pelwick</strong> III</p>

    <ul class="contact-list">
      <li>Phone: (555) 318-2276</li>
      <li>Fax: (555) 462-7093</li>
      <li>Email: Gerald@G<strong>PelwickCPA</strong>.example</li>
    </ul>

    <address class="address">
      5136 Orvale Road West, Suite D,<br>
      Larkmoor, GA 34917
    </address>
  </section>
</body>
</html>
```